Referring Dentists Referral Card

Corwell Pediatric & Teen Dentistry is looking for a new referral card to give to dentists sending their patients to our office for special treatment. Corwell Pediatric & Teen Dentistry is a modern, fun, and safe environment for children and teens to receive and experience the highest quality of dental care available. At CPTD we believe in shaping a positive experience for your child so they look forward to and love coming to the dentist!

Target Market(s)

Dentists

Industry/Entity Type

Dental

Font styles to use
Sans Serif

Colors
0292cd
acd036
f37122

Requirements
Must have
• Logo, phone number, copy from file "Referral Card In"

```html
<!DOCTYPE html>
<html lang="en">
<head>
<meta charset="utf-8">
<title>Corwell Pediatric &amp; Teen Dentistry – Referral Card</title>
<link rel="stylesheet" href="https://fonts.googleapis.com/css2?family=Quicksand:wght@400;500;600;700&family=Cinzel:wght@400&display=swap">
<style>
  :root{
    --stage:#e3e4e5;
    --label:#8a8b8d;
    --teal:#11899f;
    --teal-light:#1a9cb6;
    --orange:#f37122;
    --green:#acd036;
    --white:#ffffff;
    --field:#eeefef;
    --field-line:#d9dbdc;
    --map:#e7e9e9;
    --ink-teal:#127f95;
  }
  *{box-sizing:border-box;margin:0;padding:0}
  html,body{width:1200px;height:754px;overflow:hidden}
  body{background:var(--stage);font-family:"Quicksand",sans-serif;position:relative}

  .side-label{position:absolute;top:26px;font-size:40px;font-weight:400;color:var(--label);letter-spacing:1px;text-align:center;width:300px}
  .side-label.outside{left:152px}
  .side-label.inside{left:740px}

  .card{position:absolute;overflow:hidden;box-shadow:0 2px 6px rgba(0,0,0,.25)}

  /* Outside */
  .card-outside{left:45px;top:86px;width:536px;height:608px;
    background:radial-gradient(ellipse at 50% 75%, var(--teal-light) 0%, var(--teal) 70%)}
  .flip{position:absolute;transform:rotate(180deg);color:var(--white)}
  .website{left:323px;top:30px;font-size:16px;font-weight:500;letter-spacing:.2px}
  .badge{left:27px;top:26px;display:flex;align-items:center;gap:6px}
  .badge-mark{width:28px;height:28px;border:2px solid var(--white);border-radius:3px}
  .badge-text{display:flex;flex-direction:column;line-height:1.05}
  .badge-text .small{font-size:6px}
  .badge-text .big{font-size:12px;font-weight:700;letter-spacing:.5px}
  .map{position:absolute;left:0;top:0;width:536px;height:304px}
  .address{left:45px;top:260px;color:#1f2a30;font-size:11px;font-weight:700;line-height:1.25;letter-spacing:.3px}
  .card-title{position:absolute;top:340px;left:0;width:100%;text-align:center;font-family:"Cinzel",serif;font-weight:400;font-size:30px;line-height:40px;color:var(--white);letter-spacing:1.5px}
  .ribbon{position:absolute;left:0;top:436px;width:100%;height:42px;background:var(--orange)}
  .ribbon::before,.ribbon::after{content:"";position:absolute;left:0;right:0;border-top:1.5px dashed rgba(255,255,255,.85)}
  .ribbon::before{top:6px}.ribbon::after{bottom:6px}
  .logo-panel{position:absolute;left:73px;top:388px;width:389px;height:136px;background:var(--white);border-radius:18px;
    display:flex;align-items:center;justify-content:center;gap:14px;box-shadow:0 2px 4px rgba(0,0,0,.15)}
  .brand-dot{width:56px;height:56px;border-radius:50%;background:var(--orange);flex:none}
  .brand-name{font-size:25px;font-weight:600;color:var(--orange);line-height:1.05}
  .doctors{position:absolute;left:0;top:540px;width:100%;display:flex;justify-content:space-between;padding:0 76px 0 71px;color:var(--white);font-size:16px;font-weight:500;line-height:20px}

  /* Inside */
  .card-inside{left:610px;top:86px;width:539px;height:610px;background:var(--teal)}
  .logo-tab{position:absolute;left:35px;top:0;width:208px;height:94px;background:var(--white);border-radius:0 0 16px 16px;
    display:flex;align-items:center;gap:8px;padding:0 12px}
  .logo-tab .brand-dot{width:36px;height:36px}
  .logo-tab .brand-name{font-size:15px}
  .reminder{position:absolute;left:371px;top:34px;color:var(--white);font-size:13px;line-height:1.3}
  .intro{position:absolute;left:40px;width:380px;text-align:center;color:var(--white);font-size:14.5px;line-height:22px}
  .intro.lead{top:110px}
  .intro.note{top:186px}
  .illustration{position:absolute;left:472px;top:170px;width:67px;height:134px;border-radius:34px 0 0 0;
    background:linear-gradient(160deg,#c8303a 0%,#e6b28e 50%,#8cc43f 100%)}
  .doctor-checks{position:absolute;top:258px;left:41px;display:flex;gap:58px;color:var(--white);font-size:16px;font-weight:500}
  .doctor-checks label{display:flex;align-items:center;gap:6px}
  .check{width:24px;height:24px;background:var(--white);border-radius:5px;flex:none}
  .form{position:absolute;left:35px;top:320px;width:469px;height:300px;background:var(--white);border-radius:6px 6px 0 0;padding:14px 9px 0}
  .field{display:flex;height:28px;background:var(--field);border:1px solid var(--field-line);margin-bottom:10px}
  .field-label{width:150px;border-right:1px solid var(--field-line);color:var(--orange);font-size:13.5px;font-weight:500;display:flex;align-items:center;padding-left:8px}
  .reasons{display:flex;gap:8px;font-size:11px;color:var(--ink-teal);font-weight:500;margin:12px 0 10px}
  .reasons label{display:flex;align-items:center;gap:5px}
  .reasons .box{width:15px;height:15px;border:1px solid var(--field-line);background:var(--field);border-radius:3px}
  .comments{height:200px;background:var(--field);border:1px solid var(--field-line);padding:12px 22px 0}
  .comments-label{font-size:13px;color:#8d9193;border-bottom:1px solid #a9adaf;padding-bottom:1px}
  .line{border-bottom:1px solid #a9adaf;height:29px}
</style>
</head>
<body>
  <div class="side-label outside">OUTSIDE</div>
  <div class="side-label inside">INSIDE</div>

  <section class="card card-outside">
    <svg class="map" viewBox="0 0 536 304" role="img" aria-label="Street map showing the office location near the lake, highways and Second Street">
      <path d="M0,110 Q268,40 536,110 L536,304 L0,304 Z" fill="var(--map)"/>
      <path d="M0,110 Q268,40 536,110" fill="none" stroke="var(--green)" stroke-width="6"/>
    </svg>
    <div class="flip website">corwellkidsdentists.com</div>
    <div class="flip badge">
      <div class="badge-mark"></div>
      <div class="badge-text"><span class="small">Specialty board member</span><span class="big">BOARD CERTIFIED</span></div>
    </div>
    <div class="flip address">418 N. HARLOW AVENUE<br>SUITE 310 CORWELL, OK 73190</div>

    <h1 class="card-title">Referral Card</h1>
    <div class="ribbon"></div>
    <div class="logo-panel">
      <span class="brand-dot"></span>
      <span class="brand-name">Corwell Pediatric<br>&amp; Teen Dentistry</span>
    </div>
    <div class="doctors"><span>Marcus Ellery, DDS MSD</span><span>Owen Traske, DDS</span></div>
  </section>

  <section class="card card-inside">
    <div class="logo-tab">
      <span class="brand-dot"></span>
      <span class="brand-name">Corwell Pediatric<br>&amp; Teen Dentistry</span>
    </div>
    <p class="reminder">Please bring this card<br>to your appointment</p>
    <p class="intro lead">Your dentist cares for the wellbeing of your child<br>by referring to the pediatric dental specialists at<br>Corwell Pediatric &amp; Teen Dentistry.</p>
    <p class="intro note">Our office does not provide<br>oral conscious sedation.</p>
    <div class="illustration" role="img" aria-label="Illustration of a hand holding a red heart"></div>
    <div class="doctor-checks">
      <label><span class="check"></span>Marcus Ellery, DDS MSD</label>
      <label><span class="check"></span>Owen Traske, DDS</label>
    </div>
    <div class="form">
      <div class="field"><span class="field-label">PATIENT NAME</span></div>
      <div class="field"><span class="field-label">REFERRING DOCTOR</span></div>
      <div class="reasons">
        <label><span class="box"></span>Consultation for General Anesthesia</label>
        <label><span class="box"></span>Complex dental needs</label>
        <label><span class="box"></span>Dental anxiety</label>
      </div>
      <div class="comments">
        <div class="comments-label">Comments:</div>
        <div class="line"></div>
        <div class="line"></div>
        <div class="line"></div>
      </div>
    </div>
  </section>
</body>
</html>
```